A revolutionary website for a revolutionary construction company

I am looking for inspirations... please help me and read the attached brief

I would like to achieve a website design that is modern, premium dynamic and drives emotions. I do not want a design that can be found on a normal template. Having that said, I would also like the utilisation of Illustrations that are relation to the company’s services…. Also would like to have illustrations dynamic when you navigate on them. So a young, dynamic and parallax design website that will show off these requirements. Also to add trust, with all pages designed.

please see attachements.
Updates

Low design quality

Target Market(s)

Please read brief

Number of Pages Required

5+ page

Font styles to use
Other font styles liked:
• Futura

Requirements
Must have
• Please read brief - colours to be matching logo colours
Nice to have
Should not have

```html
<!DOCTYPE html>
<html lang="en">
<head>
<meta charset="utf-8">
<title>Keystone Build — Constructed Beyond Belief</title>
<link href="https://fonts.googleapis.com/css2?family=Montserrat:wght@400;500;600;700&family=Arimo:wght@400;700&display=swap" rel="stylesheet">
<style>
:root{
  --brand:#9e0a3b;
  --brand-dark:#4a0a1e;
  --ink:#3a3a3a;
  --muted:#555;
  --paper:#f3f3f3;
  --footer:#2f2c2d;
  --white:#fff;
}
*{margin:0;padding:0;box-sizing:border-box}
html,body{width:1200px;height:3060px;overflow:hidden}
body{position:relative;background:var(--paper);font-family:"Arimo",Arial,sans-serif;color:var(--ink)}
.abs{position:absolute}
.heading{font-family:"Montserrat",sans-serif;font-weight:700;color:var(--brand)}
.btn{position:absolute;display:flex;align-items:center;justify-content:center;background:var(--brand);color:var(--white);
  font-family:"Montserrat",sans-serif;font-weight:600;font-size:11px;letter-spacing:1.2px;border-radius:20px;
  box-shadow:0 0 0 2px var(--paper),0 0 0 3.5px var(--brand)}
.art{position:absolute;inset:0;width:1200px;height:3060px}
/* header */
.brand-mark{left:173px;top:11px;width:74px;height:74px;border-radius:50%;background:var(--white);display:flex;align-items:center;justify-content:center;
  font-family:"Montserrat",sans-serif;font-weight:700;font-size:10px;color:var(--brand);letter-spacing:.5px}
.main-nav{left:333px;top:34px;font-family:"Montserrat",sans-serif;font-weight:500;font-size:11px;letter-spacing:.8px;color:var(--white)}
.main-nav span{position:absolute;white-space:nowrap}
.main-nav .active::after{content:"";position:absolute;left:0;right:0;top:22px;height:2px;background:var(--white)}
.phone{left:877px;top:33px;font-family:"Montserrat",sans-serif;font-size:14px;color:var(--brand);font-weight:500;letter-spacing:.5px}
/* hero */
.hero-kicker{left:646px;top:259px;font-family:"Montserrat",sans-serif;font-weight:600;font-size:17px;color:#444}
.hero-title{left:643px;top:282px;font-size:47px;letter-spacing:.5px;white-space:nowrap}
.hero-copy{left:647px;top:348px;width:360px;font-size:14px;line-height:17px;color:#444}
/* services */
.section-mark{width:20px;height:20px;background:#555}
.section-title{font-size:37px;text-align:center;width:1200px;left:0}
.section-lead{width:1200px;left:0;text-align:center;font-size:14px;line-height:18px;color:#444}
.service{position:absolute;width:220px;text-align:center;font-family:"Montserrat",sans-serif;font-weight:500;font-size:12.5px;letter-spacing:1.3px;color:#555}
.service.current{color:var(--brand)}
.rule{left:173px;top:1003px;width:853px;height:1px;background:#bbb}
/* about */
.about-title{font-size:36px;line-height:44px}
.underline{height:2px;width:64px;background:var(--brand)}
.body-copy{font-size:12px;line-height:17px;color:#555}
/* numbers */
.numbers-title{left:174px;top:1853px;font-family:"Montserrat",sans-serif;font-weight:700;font-size:27px;color:var(--white)}
.stat{position:absolute;color:var(--white)}
.stat-value{font-family:"Montserrat",sans-serif;font-size:27px;font-weight:400;margin-top:12px}
.stat-note{font-size:11.5px;line-height:17px;margin-top:8px}
/* projects */
.project-frame{position:absolute;top:2449px;width:272px;height:219px;background:var(--white);padding:6px;box-shadow:0 1px 3px rgba(0,0,0,.08)}
.project-frame div{width:100%;height:100%}
.pager{left:580px;top:2721px;width:40px;text-align:center;font-family:"Montserrat",sans-serif;font-size:17px;line-height:22px;color:var(--brand);font-weight:600;white-space:nowrap}
/* footer */
.site-footer{left:0;top:2825px;width:1200px;height:235px;background:var(--footer);color:var(--white)}
.foot-h{position:absolute;top:32px;font-family:"Montserrat",sans-serif;font-weight:700;font-size:13px}
.foot-t{position:absolute;font-size:11px;line-height:14px}
.foot-rule{position:absolute;left:0;top:189px;width:1200px;height:1px;background:#555}
.social{position:absolute;top:80px;width:24px;height:24px;border-radius:50%;background:var(--brand)}
</style>
</head>
<body>

<svg class="art" viewBox="0 0 1200 3060">
  <defs>
    <linearGradient id="skyline" x1="0" y1="0" x2="0.4" y2="1">
      <stop offset="0" stop-color="#6f6d70"/>
      <stop offset="0.3" stop-color="#e6a23b"/>
      <stop offset="0.55" stop-color="#c2561b"/>
      <stop offset="1" stop-color="#3a2a28"/>
    </linearGradient>
    <linearGradient id="worker" x1="0" y1="0" x2="1" y2="1">
      <stop offset="0" stop-color="#d5623a"/>
      <stop offset="0.4" stop-color="#2d3446"/>
      <stop offset="0.75" stop-color="#8d8a86"/>
      <stop offset="1" stop-color="#c45b23"/>
    </linearGradient>
    <linearGradient id="welding" x1="0" y1="0" x2="1" y2="1">
      <stop offset="0" stop-color="#2a6a88"/>
      <stop offset="0.45" stop-color="#0d1d2b"/>
      <stop offset="1" stop-color="#06080c"/>
    </linearGradient>
  </defs>
  <polygon points="0,0 798,0 0,838" fill="url(#skyline)" role="img" aria-label="City skyline at sunset with a tall tower and a crane"/>
  <polygon points="0,720 289,535 0,838" fill="#9e0a3b" opacity=".8"/>
  <rect x="57" y="1165" width="222" height="648" fill="#ebebeb"/>
  <rect x="0" y="1370" width="16" height="443" fill="#ebebeb"/>
  <rect x="320" y="1550" width="222" height="263" fill="#ebebeb"/>
  <rect x="585" y="1410" width="150" height="403" fill="#ebebeb"/>
  <polygon points="944,1118 1090,1118 1031,1197 560,1813 404,1813" fill="#9e0a3b"/>
  <polygon points="1031,1197 1200,1197 1200,1813 560,1813" fill="url(#worker)" role="img" aria-label="Construction worker in an orange hard hat carrying a heavy pipe"/>
  <polygon points="1031,1197 1060,1197 640,1813 560,1813" fill="#9e0a3b" opacity=".65"/>
  <rect x="0" y="1813" width="1200" height="310" fill="#9e0a3b"/>
  <rect x="383" y="1913" width="176" height="164" fill="#4a0a1e"/>
  <polygon points="0,2123 493,2123 0,2825" fill="url(#welding)" role="img" aria-label="Welder at work with sparks flying"/>
  <polygon points="300,2450 370,2420 0,2825 0,2800" fill="#9e0a3b" opacity=".85"/>
  <polygon points="0,2560 200,2440 240,2440 0,2720" fill="#9e0a3b" opacity=".55"/>

  <g fill="none" stroke="#9e0a3b" stroke-width="1.6">
    <circle cx="277" cy="867" r="54"/>
    <circle cx="697" cy="867" r="54"/>
    <circle cx="927" cy="867" r="54"/>
  </g>
  <circle cx="485" cy="867" r="55" fill="#9e0a3b"/>
  <g fill="none" stroke="#9e0a3b" stroke-width="2" stroke-linejoin="round" stroke-linecap="round">
    <path d="M259 864 L277 848 L295 864 M263 860 V886 H291 V860"/>
    <path d="M277 872 l6 -6 l4 4 l-6 6 z"/>
    <rect x="679" y="853" width="26" height="32" rx="2"/>
    <path d="M686 851 h12 v5 h-12 z M684 863 l2 2 l4 -4 M684 873 l2 2 l4 -4"/>
    <circle cx="708" cy="880" r="9"/><path d="M708 875 v5 h4"/>
    <circle cx="927" cy="871" r="15"/><path d="M922 852 h10 M927 852 v4 M940 857 l3 -3"/>
    <text x="927" y="876" text-anchor="middle" font-family="Montserrat,sans-serif" font-size="11" fill="#9e0a3b" stroke="none" font-weight="700">24</text>
  </g>
  <g fill="none" stroke="#fff" stroke-width="2" stroke-linejoin="round">
    <path d="M474 858 a11 11 0 0 1 22 0 z M471 858 h28"/>
    <path d="M470 888 v-10 a6 6 0 0 1 6 -6 h18 a6 6 0 0 1 6 6 v10 M479 872 v16 M491 872 v16"/>
  </g>

  <g fill="none" stroke="#fff" stroke-width="1.8" stroke-linejoin="round">
    <path d="M178 1948 l10 -22 l12 22 z M178 1948 h32 M190 1928 l8 10"/>
    <circle cx="413" cy="1932" r="5"/><circle cx="428" cy="1930" r="5"/><circle cx="443" cy="1932" r="5"/>
    <path d="M406 1946 a7 7 0 0 1 14 0 M421 1944 a7 7 0 0 1 14 0 M436 1946 a7 7 0 0 1 14 0"/>
    <path d="M644 1930 l14 -6 l14 6 l-14 6 z"/><circle cx="658" cy="1938" r="5"/><path d="M648 1952 v-3 a10 6 0 0 1 20 0 v3 z"/>
    <path d="M895 1948 a15 15 0 0 1 30 0 z M891 1948 h38 M910 1933 v-6"/>
  </g>
  <g fill="none" stroke="#888" stroke-width="3" stroke-linecap="round">
    <path d="M566 2724 l-7 8 l7 8"/><path d="M634 2724 l7 8 l-7 8"/>
  </g>
</svg>

<header class="site-header">
  <div class="abs brand-mark">KEYSTONE</div>
  <nav class="abs main-nav">
    <span class="active" style="left:0">HOME</span>
    <span style="left:66px">ABOUT US</span>
    <span style="left:153px">SERVICES</span>
    <span style="left:238px">PROJECTS</span>
    <span style="left:324px">CONTACT US</span>
  </nav>
  <div class="abs phone">+1(555) 014-0288</div>
  <div class="btn" style="left:860px;top:66px;width:164px;height:32px;font-size:12px">CALL US TODAY</div>
</header>

<section class="hero">
  <div class="abs hero-kicker">Constructed</div>
  <h1 class="abs heading hero-title">Beyond Belief</h1>
  <p class="abs hero-copy">Lorem ipsum dolor sit amet, consectetur adipiscing elit, sed do eiusmod tempor incididunt ut labore et dolore magna aliqua.</p>
  <div class="btn" style="left:648px;top:429px;width:166px;height:33px">FIND OUT MORE</div>
</section>

<section class="services">
  <div class="abs section-mark" style="left:590px;top:645px"></div>
  <h2 class="abs heading section-title" style="top:676px">Services we provide</h2>
  <p class="abs section-lead" style="top:736px">Ut enim ad minim veniam, quis nostrud exercitation ullamco laboris<br>nisi ut aliquip ex ea commodo consequat.</p>
  <div class="service" style="left:167px;top:946px">DESIGN AND CONSTRUCT</div>
  <div class="service current" style="left:375px;top:946px">CONSTRUCTION</div>
  <div class="service" style="left:587px;top:946px">PROJECT MANAGEMENT</div>
  <div class="service" style="left:817px;top:946px">24-HR SERVICE CALLS</div>
  <div class="abs rule"></div>
</section>

<section class="about">
  <h2 class="abs heading about-title" style="left:173px;top:1082px">We build your dreams</h2>
  <div class="abs underline" style="left:173px;top:1142px"></div>
  <p class="abs body-copy" style="left:173px;top:1182px;width:275px">Lorem ipsum dolor sit amet, consectetur adipiscing elit, sed do eiusmod tempor incididunt ut labore et dolore magna aliqua. Ut enim ad minim veniam, quis nostrud exercitation ullamco laboris nisi ut aliquip ex ea commodo consequat. Duis aute irure dolor in reprehenderit in voluptate velit esse cillum dolore eu fugiat nulla pariatur. Excepteur sint occaecat cupidatat non proident, sunt in culpa qui officia deserunt mollit anim id est laborum.</p>
  <p class="abs body-copy" style="left:482px;top:1182px;width:285px">The passage experienced a surge in popularity during the 1960s when Typeline used it on their dry-transfer sheets, and again during the 90s as desktop publishers bundled the text with their software. Today it's seen all around the web; on templates, websites, and stock designs. Use our generator to get your own, or read on for the authoritative history of lorem ipsum. A practice not without controversy, laying out pages with meaningless filler text can.</p>
  <h2 class="abs heading about-title" style="left:173px;top:1372px">Managing through<br>changing time</h2>
  <div class="abs underline" style="left:173px;top:1478px"></div>
  <p class="abs body-copy" style="left:173px;top:1511px;width:335px">Lorem ipsum dolor sit amet, consectetur adipiscing elit, sed do eiusmod tempor incididunt ut labore et dolore magna aliqua. Ut enim ad minim veniam, quis nostrud exercitation ullamco laboris nisi ut aliquip ex ea commodo consequat. Duis aute irure dolor in reprehenderit in voluptate velit esse cillum dolore eu fugiat nulla pariatur. Excepteur sint occaecat cupidatat non proident, sunt in culpa qui officia deserunt mollit anim id est laborum.</p>
  <div class="btn" style="left:172px;top:1684px;width:162px;height:32px">FIND OUT MORE</div>
</section>

<section class="numbers">
  <h2 class="abs numbers-title">Our business in numbers</h2>
  <div class="stat" style="left:174px;top:1956px"><div class="stat-value">£ 1.1 bn</div><div class="stat-note">revenue and a major<br>contractor across the UK</div></div>
  <div class="stat" style="left:409px;top:1956px"><div class="stat-value">3,000</div><div class="stat-note">passionate and talented<br>employees across the UK</div></div>
  <div class="stat" style="left:643px;top:1956px"><div class="stat-value">8.2 %</div><div class="stat-note">of our people are apprentices,<br>graduates or trainees</div></div>
  <div class="stat" style="left:893px;top:1956px"><div class="stat-value">0.07</div><div class="stat-note">AFR reflecting our<br>commitment to excellent<br>health and safety</div></div>
</section>

<section class="projects">
  <div class="abs section-mark" style="left:590px;top:2251px"></div>
  <h2 class="abs heading section-title" style="top:2282px">Our Latest Projects</h2>
  <div class="abs underline" style="left:568px;top:2338px"></div>
  <p class="abs section-lead" style="top:2353px;font-size:12px;line-height:17px;color:#555">Lorem ipsum dolor sit amet, consectetur adipiscing elit, sed do eiusmod<br>tempor incididunt ut labore et dolore magna aliqua.</p>
  <div class="project-frame" style="left:173px"><div role="img" aria-label="Modern white villa with dark timber balconies" style="background:linear-gradient(160deg,#8fb7d8,#d9dde0 45%,#5a5350)"></div></div>
  <div class="project-frame" style="left:465px"><div role="img" aria-label="Stone-clad house at sunset beside a lake" style="background:linear-gradient(160deg,#e9e2d2,#8a8277 50%,#3c3732)"></div></div>
  <div class="project-frame" style="left:759px"><div role="img" aria-label="White manor house with a driveway among trees" style="background:linear-gradient(160deg,#b9c3cc,#e8e8e6 45%,#5d6a44)"></div></div>
  <div class="abs pager">1 / 4</div>
</section>

<footer class="abs site-footer">
  <div class="foot-h" style="left:173px">About Us</div>
  <p class="foot-t" style="left:173px;top:70px;width:195px">Lorem ipsum dolor sit amet, conse ctetur adipiscing elit, sed do eiusmod tempor incididunt ut labore et dolore magna aliqua.</p>
  <div class="foot-h" style="left:399px">Our Address</div>
  <p class="foot-t" style="left:399px;top:70px">12/8 Fernhill Avenue<br>Linden Town, Austria<br><br>Phone: 55501234<br>Email: hello@keystonebuild.test<br>Office Time: 10AM- 5PM</p>
  <div class="foot-h" style="left:575px">Quick Links</div>
  <p class="foot-t" style="left:575px;top:70px;line-height:20px">About us<br>Our services<br>Contact us<br>Meet team</p>
  <p class="foot-t" style="left:678px;top:70px;line-height:20px">Privacy Policy<br>Testimonials<br>News<br>FAQ</p>
  <div class="foot-h" style="left:821px">Follow Us</div>
  <div class="social" style="left:821px"></div>
  <div class="social" style="left:851px"></div>
  <div class="social" style="left:882px"></div>
  <div class="foot-rule"></div>
  <p class="foot-t" style="left:173px;top:206px;font-size:10px">Copyright © 2020 Keystone Build . All Rights Reserved</p>
  <p class="foot-t" style="left:879px;top:206px;font-size:10px">Terms of Use &nbsp;| &nbsp; Privacy Policy</p>
</footer>

</body>
</html>
```